Girls Night Out Flyer for a female oriented event

I need a flyer to promote my event which should look "FUN" and "Sophisticated"
I would need the flyer to be 8 1/2" X 11" 300 dpi. I would need the layered .psd file as well as all the fonts. The flyer should contain the following info:

Velvet Evening Soiree CT
Friday, September 25th
6:00-10:00 PM
The Willow Hall Pavilion
14 Marlow Rd
Danbury, CT 06811
First 100 guests will have a chance to win $25,000 and receive a swag bag filled with gifts
$20 Advanced Admission at www.velveteveningsoireect.com
$25 at the door
(Key words)
Martini Bar
Wine Tasting
Food Sampling
Beauty Make-Overs
Fashion Shows
Psychic Readings
Shopping
Door Prizes
Swag Bag
Exhibitors
For tickets visit www.velveteveningsoireect.com

Target Market(s)

Ladies

Industry/Entity Type

Event

Requirements
Must have
• see description

```html
<!DOCTYPE html>
<html lang="en">
<head>
<meta charset="utf-8">
<title>Velvet Evening Soiree CT — Flyer</title>
<link rel="stylesheet" href="https://fonts.googleapis.com/css2?family=Montserrat:wght@300;400;700&family=Raleway:wght@200;300&display=swap">
<style>
  :root {
    --paper: #f3f1f1;
    --paper-deep: #e6e2e2;
    --pink: #e8174f;
    --maroon: #7c1c3c;
    --crimson: #c0285a;
    --ink: #3a3033;
    --ink-soft: #4b4245;
    --gown-gold: #d9b99a;
    --skin: #e8c6b3;
  }
  * { margin: 0; padding: 0; box-sizing: border-box; }
  html, body { width: 927px; height: 1200px; overflow: hidden; background: var(--paper); }
  .flyer {
    position: relative;
    width: 927px;
    height: 1200px;
    overflow: hidden;
    background: radial-gradient(ellipse at 70% 30%, #ffffff 0%, var(--paper) 55%, var(--paper-deep) 100%);
    font-family: "Montserrat", sans-serif;
  }
  .portrait {
    position: absolute;
    left: 430px;
    top: 0;
    width: 497px;
    height: 1200px;
    background:
      radial-gradient(ellipse 40% 18% at 68% 20%, var(--skin) 0%, rgba(232,198,179,0) 100%),
      radial-gradient(ellipse 45% 22% at 75% 12%, rgba(90,58,42,0.55) 0%, rgba(90,58,42,0) 100%),
      linear-gradient(180deg, rgba(255,255,255,0) 30%, var(--gown-gold) 60%, #e9e1da 100%);
    opacity: 0.9;
  }
  .date { position: absolute; left: 73px; top: 66px; color: var(--crimson); }
  .date-month { font-family: "Raleway", sans-serif; font-weight: 300; font-size: 26px; letter-spacing: 0.5px; line-height: 1; }
  .date-day { font-family: "Raleway", sans-serif; font-weight: 200; font-size: 118px; line-height: 0.9; color: var(--maroon); margin-left: -4px; position: relative; }
  .date-day sup { position: absolute; left: 160px; top: -4px; font-size: 13px; font-weight: 300; color: var(--crimson); }
  .date-weekday { font-family: "Raleway", sans-serif; font-weight: 300; font-size: 40px; line-height: 1.05; }
  .date-time { font-size: 15px; font-weight: 400; color: var(--ink); margin-top: 4px; }
  .venue {
    position: absolute; left: 282px; top: 96px; width: 270px;
    font-family: "Montserrat", sans-serif; font-weight: 400; font-size: 26px; line-height: 1.25;
    color: var(--ink);
  }
  .title {
    position: absolute; left: 66px; top: 318px;
    font-family: "Montserrat", sans-serif; font-weight: 700; font-size: 84px;
    color: var(--pink); line-height: 1.0; letter-spacing: -1px;
  }
  .title span { display: block; }
  .offer { position: absolute; left: 69px; top: 686px; color: var(--crimson); font-size: 31px; font-weight: 300; line-height: 1.36; text-transform: uppercase; }
  .offer strong { font-weight: 700; }
  .features {
    position: absolute; left: 71px; top: 982px; width: 820px;
    font-size: 17.5px; font-weight: 400; color: var(--ink-soft); line-height: 1.12; text-transform: uppercase; word-spacing: 2px;
  }
  .features span { margin-right: 22px; }
  .admission { position: absolute; left: 70px; top: 1068px; font-size: 21px; font-weight: 700; color: var(--maroon); line-height: 1.25; text-transform: uppercase; }
  .address { position: absolute; left: 71px; top: 1142px; font-size: 13px; color: var(--ink-soft); text-transform: uppercase; }
</style>
</head>
<body>
<main class="flyer">
  <div class="portrait" role="img" aria-label="Photograph of a glamorous woman in a strapless crystal-embellished gown against a white quilted backdrop"></div>

  <div class="date">
    <div class="date-month">SEPTEMBER</div>
    <div class="date-day">25<sup>th</sup></div>
    <div class="date-weekday">FRIDAY</div>
    <div class="date-time">6:00 – 10:00 PM</div>
  </div>

  <div class="venue">The Willow Hall Pavilion</div>

  <h1 class="title">
    <span>Velvet</span>
    <span>Evening</span>
    <span>Soiree CT</span>
  </h1>

  <p class="offer">
    <strong>First 100 guests</strong><br>
    will have a chance<br>
    to win <strong>$25,000</strong><br>
    and receive<br>
    a swag bag<br>
    filled with gifts
  </p>

  <p class="features">
    <span>Martini Bar</span><span>Wine Tasting</span><span>Food Sampling</span><span>Beauty Make-Overs</span><br>
    <span>Fashion Shows</span><span>Psychic Readings</span><span>Shopping</span><span>Door Prizes</span><br>
    <span>Swag Bag</span><span>Exhibitors</span><span>For tickets visit www.velveteveningsoireect.com</span>
  </p>

  <p class="admission">
    $20 Advanced Admission at www.velveteveningsoireect.com<br>
    $25 at the door
  </p>

  <p class="address">14 Marlow Rd. Danbury, CT 06811</p>
</main>
</body>
</html>
```